Business Card cabinets and cabinets components making company.

the card should be formal and interesting at the same time. The main colors will be black and white.

Font styles to use
Sans Serif

Colors

Designer to choose only greyscale colors for use in the design.

Requirements
Must have
• At least must have the followings:
office phone
cell phone
address
position
name
email
web

```html
<!DOCTYPE html>
<html lang="en">
<head>
<meta charset="utf-8">
<title>Trimfold Business Card</title>
<link rel="stylesheet" href="https://fonts.googleapis.com/css2?family=Open+Sans:wght@700&family=Roboto:wght@400;500&display=swap">
<style>
  :root {
    --bg: #5a5a5a;
    --card: #1b1b1c;
    --card-edge: #232324;
    --band: #3d3c3d;
    --band-dark: #302f30;
    --white: #ffffff;
    --muted: #d6d6d6;
    --gloss: #6f6f71;
    --ghost: #262627;
  }
  * { box-sizing: border-box; margin: 0; padding: 0; }
  html, body { width: 799px; height: 1200px; overflow: hidden; }
  body {
    background: var(--bg);
    font-family: "Roboto", sans-serif;
    position: relative;
  }
  .card {
    position: absolute;
    left: 80px;
    width: 640px;
    height: 366px;
    background: var(--card);
    border-radius: 6px;
    overflow: hidden;
    box-shadow: 0 10px 30px rgba(0,0,0,.45);
  }
  .card--front { top: 120px; }
  .card--back { top: 690px; }

  .brand {
    display: flex;
    align-items: center;
    gap: 14px;
    font-family: "Roboto", sans-serif;
    font-weight: 500;
    letter-spacing: 1px;
  }
  .brand__mark { display: block; border: 4px solid currentColor; }

  .card--front .brand {
    position: absolute;
    left: 50%;
    top: 50%;
    transform: translate(-50%, -50%);
    color: var(--gloss);
    font-size: 78px;
  }
  .card--front .brand__mark { width: 58px; height: 58px; }

  .card--back .brand {
    position: absolute;
    left: 48px;
    top: 98px;
    color: var(--white);
    font-size: 50px;
  }
  .card--back .brand__mark { width: 38px; height: 38px; border-width: 3px; }

  .ghost-square {
    position: absolute;
    right: 40px;
    top: 40px;
    width: 200px;
    height: 200px;
    background: var(--ghost);
  }

  .band {
    position: absolute;
    left: 0; bottom: 0;
    width: 640px; height: 110px;
  }

  .contact {
    position: absolute;
    left: 370px;
    top: 100px;
    width: 250px;
    color: var(--white);
  }
  .contact__name {
    font-family: "Open Sans", sans-serif;
    font-weight: 700;
    font-size: 22px;
    line-height: 1.1;
  }
  .contact__role { font-size: 14px; color: var(--muted); margin-top: 2px; }
  .contact__address {
    font-size: 14px;
    line-height: 1.3;
    margin-top: 14px;
    padding-bottom: 8px;
    border-bottom: 1.5px solid var(--white);
  }
  .contact__list { list-style: none; margin-top: 8px; }
  .contact__list li {
    display: flex;
    align-items: center;
    gap: 10px;
    font-size: 14px;
    line-height: 1.45;
  }
  .contact__list svg { width: 13px; height: 13px; fill: var(--white); flex: none; }

  .web {
    position: absolute;
    left: 250px;
    bottom: 40px;
    color: var(--white);
    font-size: 15px;
    letter-spacing: .3px;
  }
</style>
</head>
<body>

<section class="card card--front" aria-label="Card front">
  <div class="brand"><span class="brand__mark"></span>Trimfold</div>
</section>

<section class="card card--back" aria-label="Card back">
  <div class="ghost-square"></div>

  <svg class="band" viewBox="0 0 640 110" aria-hidden="true">
    <path d="M0 30 H190 Q200 30 205 40 L215 58 H640 V110 H0 Z" fill="var(--band-dark)"/>
    <path d="M0 40 H188 Q196 40 200 48 L210 66 H640 V110 H0 Z" fill="var(--band)"/>
  </svg>

  <div class="brand"><span class="brand__mark"></span>Trimfold</div>

  <div class="contact">
    <p class="contact__name">Mark Ellison</p>
    <p class="contact__role">Managing Director</p>
    <p class="contact__address">88 Harbor Lane, Fair City,<br>Any Town, US 654321</p>
    <ul class="contact__list">
      <li>
        <svg viewBox="0 0 24 24" aria-hidden="true"><path d="M6.6 10.8a15 15 0 0 0 6.6 6.6l2.2-2.2a1 1 0 0 1 1-.25 11.4 11.4 0 0 0 3.6.57 1 1 0 0 1 1 1V20a1 1 0 0 1-1 1A17 17 0 0 1 3 4a1 1 0 0 1 1-1h3.5a1 1 0 0 1 1 1c0 1.25.2 2.45.57 3.57a1 1 0 0 1-.25 1z"/></svg>
        2222-222-2222
      </li>
      <li>
        <svg viewBox="0 0 24 24" aria-hidden="true"><path d="M7 1h10a2 2 0 0 1 2 2v18a2 2 0 0 1-2 2H7a2 2 0 0 1-2-2V3a2 2 0 0 1 2-2zm0 3v14h10V4zm5 15.5a1.2 1.2 0 1 0 0 2.4 1.2 1.2 0 0 0 0-2.4z"/></svg>
        3333-333-3333
      </li>
      <li>
        <svg viewBox="0 0 24 24" aria-hidden="true"><path d="M2 5h20v14H2zm2 2v.5l8 5 8-5V7zm0 2.9V17h16V9.9l-8 5z"/></svg>
        mark@trimfold.com
      </li>
    </ul>
  </div>

  <p class="web">www.trimfold.com</p>
</section>

</body>
</html>
```